Brom-leigh Sky Harbour Custom Brokers Limited

Shop online from the USA and Ship to Jamaica
Customs Brokerage, Import Export and logistic Services
Address:- 238-240 Halden Brook Road Kingston Jamaica
Email: info@bromleighskyharbour,com
Web: www.bromleighskyharbour.com
Telephone: (876) 555-0148, (876) 555-0193
flyer should be quarter page must print information on back and front

```html
<!DOCTYPE html>
<html lang="en">
<head>
<meta charset="utf-8">
<title>Brom-leigh Sky Harbour Custom Brokers – Flyer Front and Back</title>
<link href="https://fonts.googleapis.com/css2?family=Open+Sans:wght@300;400;600;700;800&family=Dancing+Script:wght@700&display=swap" rel="stylesheet">
<style>
  :root{
    --backdrop:#13202a;
    --navy:#13305a;
    --blue:#2b6cbf;
    --gold:#e8ab22;
    --gold-deep:#d99a12;
    --paper:#ffffff;
    --mist:#e9ebee;
    --ink:#1d1d1d;
    --grey-text:#4a4a4a;
    --light-text:#b5b5b5;
    --footer-grey:#d3d6d8;
  }
  *{box-sizing:border-box;margin:0;padding:0}
  html,body{width:1200px;height:840px;overflow:hidden;background:var(--backdrop)}
  body{position:relative;font-family:"Open Sans",Arial,sans-serif;color:var(--ink)}

  .page{position:absolute;top:95px;width:466px;height:659px;background:var(--paper);overflow:hidden;box-shadow:0 6px 18px rgba(0,0,0,.45)}
  .page--front{left:124px}
  .page--back{left:638px;background:var(--mist)}

  /* ---------- front ---------- */
  .brand{position:absolute;left:34px;top:22px;width:150px;text-align:center}
  .brand__row{display:flex;align-items:center;justify-content:center;gap:6px}
  .brand__dot{width:22px;height:22px;border-radius:50%;background:var(--gold);flex:none}
  .brand__name{font-weight:800;font-size:13px;line-height:1.1;color:var(--navy);text-align:left;letter-spacing:.3px}
  .brand__tag{font-size:6.5px;letter-spacing:2.6px;color:#8a8a8a;margin-top:5px}

  .contact-note{position:absolute;left:226px;top:23px;width:222px;text-align:right;font-weight:300;font-size:18px;line-height:21px;color:var(--light-text)}

  .top-stripe{position:absolute;left:0;top:77px;width:466px;height:11px}

  .hero-photo{position:absolute;left:0;top:88px;width:466px;height:244px;
    background:linear-gradient(160deg,#f2c7a0 0%,#9bb8c2 30%,#3f7d8f 60%,#2d5e6e 100%)}
  .hero-panel{position:absolute;left:0;top:88px;width:466px;height:244px}
  .hero-title{position:absolute;left:28px;top:115px;font-weight:700;font-size:26px;line-height:31px;color:#fff;text-shadow:0 1px 3px rgba(0,0,0,.25)}
  .hero-rule{position:absolute;left:28px;top:249px;width:84px;height:3px;background:var(--gold-deep);filter:brightness(.85)}

  .web-band{position:absolute;left:0;top:332px;width:466px;height:45px;background:var(--navy)}
  .web-band__url{position:absolute;left:18px;top:12px;font-weight:700;font-size:15px;color:#fff;white-space:nowrap}
  .register{position:absolute;left:253px;top:332px;width:213px;height:63px}
  .register__text{position:absolute;left:265px;top:341px;width:192px;text-align:right;color:#fff;font-weight:300;font-size:19.5px;line-height:22px}
  .register__text strong{font-weight:700}

  .services-list{position:absolute;left:23px;top:406px;font-weight:300;font-size:24px;line-height:32.4px;color:var(--ink)}
  .divider{position:absolute;left:178px;top:411px;width:2px;height:159px;background:#d9d9d9}
  .about{position:absolute;left:193px;top:409px;width:256px}
  .about__name{font-weight:700;font-size:15.5px;color:var(--gold);letter-spacing:.2px}
  .about__body{margin-top:7px;font-size:9.6px;line-height:13.4px;color:var(--grey-text)}

  .social-bar{position:absolute;left:0;top:589px;width:466px;height:36px;background:var(--navy)}
  .social-bar__follow{position:absolute;left:18px;top:5px;font-family:"Dancing Script",cursive;font-size:12px;line-height:11px;color:var(--gold);transform:rotate(-8deg)}
  .social-bar__icons{position:absolute;left:60px;top:8px;display:flex;gap:7px}
  .social-bar__icons span{width:20px;height:20px;border:1.5px solid #fff;border-radius:50%}
  .social-bar__contact{position:absolute;right:22px;top:6px;font-weight:300;font-size:18px;color:#fff}
  .social-bar__contact b{font-weight:700;color:var(--gold)}

  .address-bar{position:absolute;left:0;top:625px;width:466px;height:34px;background:var(--footer-grey);font-size:11.5px}
  .address-bar__home{position:absolute;left:18px;top:6px}
  .address-bar__addr{position:absolute;left:52px;top:9px;font-style:italic;font-weight:600;color:var(--ink)}
  .address-bar__phone{position:absolute;right:22px;top:6px;display:flex;align-items:center;gap:6px;font-size:13px;color:var(--ink)}
  .phone-dot{width:17px;height:17px;border-radius:50%;background:var(--gold);display:flex;align-items:center;justify-content:center}

  /* ---------- back ---------- */
  .services-head{position:absolute;left:0;top:14px;width:466px;height:33px;background:var(--gold);text-align:center;color:#fff;font-weight:800;font-size:24px;line-height:33px;letter-spacing:.5px;text-shadow:0 1px 2px rgba(0,0,0,.25)}
  .services-area{position:absolute;left:0;top:47px;width:466px;height:345px;background:linear-gradient(180deg,#f1f2f3,#e3e5e7)}
  .services-graphic{position:absolute;left:0;top:0}
  .hub-name{position:absolute;left:162px;top:157px;width:150px;text-align:center;font-weight:800;font-size:15px;line-height:17px;color:var(--navy)}

  .service{position:absolute;width:120px;text-align:center}
  .service h3{font-weight:700;font-size:14px;line-height:17px;color:var(--ink)}
  .service p{font-size:8.6px;line-height:11px;color:var(--grey-text);margin-top:3px}
  .service--shipping{left:26px;top:44px}
  .service--imports{left:324px;top:55px}
  .service--logistics{left:18px;top:135px}
  .service--export{left:327px;top:135px}
  .service--customs{left:152px;top:254px;width:170px}

  .photo-disc{position:absolute;width:126px;height:126px;border-radius:50%}
  .photo-disc--boxes{left:25px;top:209px;background:radial-gradient(circle at 50% 45%,#d6a96a,#b88548 60%,#e6e2dc 100%)}
  .photo-disc--hands{left:328px;top:204px;background:radial-gradient(circle at 50% 55%,#d9a867,#a8783f 55%,#5f89b8 100%)}

  .scene-photo{position:absolute;left:0;top:392px;width:466px;height:234px;
    background:linear-gradient(100deg,#8d6f5a 0%,#c9925a 30%,#d9b690 55%,#b48a6e 75%,#6b4d3d 100%)}
  .scene-brand{position:absolute;left:90px;top:468px;width:170px;text-align:center}
  .scene-brand .brand__name{color:var(--navy);font-size:14px;text-align:center}

  .back-footer{position:absolute;left:0;top:626px;width:466px;height:33px;background:var(--navy);text-align:center;color:#fff;font-weight:700;font-size:17.5px;line-height:33px;letter-spacing:2px}
</style>
</head>
<body>

<section class="page page--front" aria-label="Flyer front">
  <div class="brand">
    <div class="brand__row">
      <span class="brand__dot"></span>
      <span class="brand__name">BROM-LEIGH<br>SKY HARBOUR</span>
    </div>
    <div class="brand__tag">Custom Brokers Ltd.</div>
  </div>

  <p class="contact-note">Please contact one of our offices for further details.</p>

  <svg class="top-stripe" viewBox="0 0 466 11" preserveAspectRatio="none">
    <polygon points="221,0 466,0 466,11 213,11" fill="var(--navy)"/>
  </svg>

  <div class="hero-photo" role="img" aria-label="Aerial photo of a container ship loaded with colourful containers sailing at sunset, with a tug boat alongside"></div>
  <svg class="hero-panel" viewBox="0 0 466 244">
    <polygon points="0,0 272,0 116,244 0,244" fill="var(--gold)"/>
    <polygon points="272,0 282,0 126,244 116,244" fill="#f2c24f" opacity=".6"/>
  </svg>
  <h1 class="hero-title">Shop online<br>from the USA<br>and Ship to<br>Jamaica</h1>
  <div class="hero-rule"></div>

  <div class="web-band"><span class="web-band__url">www.BromleighSkyHarbour.com</span></div>
  <svg class="register" viewBox="0 0 213 63">
    <polygon points="33,0 213,0 213,63 0,63" fill="var(--blue)"/>
  </svg>
  <p class="register__text">NOW AVAILABLE<br>ONLINE <strong>REGISTER</strong></p>

  <p class="services-list">Customs<br>Brokerage,<br>Import Export<br>and logistic<br>Services</p>
  <div class="divider"></div>
  <div class="about">
    <h2 class="about__name">BROM-LEIGH SKY HARBOUR</h2>
    <p class="about__body">Sed ut perspiciatis unde omnis iste natus error sit voluptatem accusantium dol orem que laudantium, totam rem aperiam, eaque ipsa quae ab illo invent ore veritatis et quasi architecto beatae vitae dicta sunt explicabo. Nemo enim ipsam voluptatem quia volupt as sit aspernatur aut odit aut fugit, sed quia consequunt ur magni dolores eos qui ratione voluptatem sequi nesciunt.Neque porro quisquam est, qui dolorem ipsum quia dolor sit amet, consectetur, adipisci velit, sed quia non numquam eius modi</p>
  </div>

  <div class="social-bar">
    <span class="social-bar__follow">Follow<br>&nbsp;us on</span>
    <div class="social-bar__icons"><span></span><span></span><span></span><span></span><span></span></div>
    <p class="social-bar__contact">Contact Us. <b>(876) 555-0193</b></p>
  </div>

  <div class="address-bar">
    <svg class="address-bar__home" width="26" height="22" viewBox="0 0 26 22">
      <polygon points="13,1 25,11 22,11 22,21 4,21 4,11 1,11" fill="#5aa7e0"/>
      <rect x="10" y="13" width="6" height="8" fill="#fff"/>
    </svg>
    <span class="address-bar__addr">238-240 Halden Brook Road Kingston Jamaica</span>
    <span class="address-bar__phone">
      <span class="phone-dot"><svg width="10" height="10" viewBox="0 0 10 10"><path d="M2 1 L4 1 L5 3 L4 4 Q5 6 6 6 L7 5 L9 6 L9 8 Q8 9 7 9 Q1 8 1 2 Q1 1 2 1Z" fill="var(--ink)"/></svg></span>
      (876) 555-0148
    </span>
  </div>
</section>

<section class="page page--back" aria-label="Flyer back">
  <h2 class="services-head">OUR SERVICES</h2>

  <div class="services-area">
    <svg class="services-graphic" width="466" height="345" viewBox="0 0 466 345">
      <defs>
        <radialGradient id="hub-fill" cx="50%" cy="40%" r="60%">
          <stop offset="0" stop-color="#ffffff"/>
          <stop offset="1" stop-color="#c9ccd0"/>
        </radialGradient>
      </defs>
      <circle cx="237" cy="126" r="108" fill="url(#hub-fill)"/>
      <path d="M172,40 A108,108 0 1,0 305,40" fill="none" stroke="var(--navy)" stroke-width="2.5"/>
      <circle cx="172" cy="40" r="4" fill="var(--navy)"/>
      <circle cx="305" cy="40" r="4" fill="var(--navy)"/>
      <path d="M30,226 A63,63 0 0,1 150,245" fill="none" stroke="var(--gold)" stroke-width="2.5"/>
      <path d="M340,230 A63,63 0 0,1 454,255" fill="none" stroke="var(--gold)" stroke-width="2.5"/>

      <g fill="var(--gold)">
        <circle cx="145" cy="65" r="14"/>
        <circle cx="326" cy="64" r="14"/>
        <circle cx="237" cy="234" r="13"/>
      </g>
      <g fill="var(--navy)">
        <circle cx="131" cy="139" r="14"/>
        <circle cx="343" cy="139" r="14"/>
      </g>
      <g fill="none" stroke="#fff" stroke-width="1.3">
        <rect x="137" y="60" width="10" height="7"/><path d="M147,62 h5 l3,3 v2 h-8"/>
        <path d="M319,70 v-8 h8 M323,66 l9,-7 M328,59 h4 v4"/>
        <rect x="232" y="228" width="10" height="12"/><path d="M235,232 h4 M235,235 h4"/>
        <path d="M124,145 v-12 h6 l4,6 v6 z M136,132 v13 h6"/>
        <circle cx="343" cy="139" r="6"/><path d="M337,139 h12 M343,133 v12"/>
      </g>
    </svg>
    <p class="hub-name">BROM-LEIGH<br>SKY HARBOUR</p>

    <div class="service service--shipping">
      <h3>Shipping</h3>
      <p>Sed Ut Perspiciatis<br>Unde Omnis Iste<br>Natus Error</p>
    </div>
    <div class="service service--imports">
      <h3>Imports</h3>
      <p>Sed ut perspiciatis<br>unde omnis iste<br>natus error</p>
    </div>
    <div class="service service--logistics">
      <h3>Logistics</h3>
      <p>Sed ut perspiciatis<br>unde omnis iste<br>natus error</p>
    </div>
    <div class="service service--export">
      <h3>Export</h3>
      <p>Sed ut perspiciatis<br>unde omnis iste<br>natus error</p>
    </div>
    <div class="service service--customs">
      <h3>Customs Clearance</h3>
      <p>Sed ut perspiciatis unde<br>omnis iste natus error</p>
    </div>

    <div class="photo-disc photo-disc--boxes" role="img" aria-label="Photo of a stack of cardboard shipping boxes from online stores"></div>
    <div class="photo-disc photo-disc--hands" role="img" aria-label="Photo of hands receiving a delivered parcel"></div>
  </div>

  <div class="scene-photo" role="img" aria-label="Photo collage of a cargo plane over stacked containers and delivery trucks, with a smiling woman shopping on a laptop"></div>
  <div class="scene-brand">
    <div class="brand__row">
      <span class="brand__dot"></span>
      <span class="brand__name">BROM-LEIGH SKY HARBOUR</span>
    </div>
  </div>

  <p class="back-footer">www.BromleighSkyHarbour.com</p>
</section>

</body>
</html>
```